Meadow Lantern Website

Here is the link for all the details, images and information you may need about our website:

https://www.filecrate.net/s/8pq42xk7m0zt3wd/OWEN%20HARGROVE.rar?dl=0

Here is a reference on our competitor: http://www.trekkora.com.au/ and we want as good as this one.

Number of Pages Required

1 page

```html
<!DOCTYPE html>
<html lang="en">
<head>
<meta charset="utf-8">
<title>Meadow Lantern – Cape Tribulation and Cairns</title>
<link href="https://fonts.googleapis.com/css2?family=Bangers&family=Rye&family=Quicksand:wght@500;600&family=Exo+2:ital,wght@1,500&family=Rosarivo&family=Sancreek&display=swap" rel="stylesheet">
<style>
:root{
  --bg:#1e140d;
  --bark:#6b3813;
  --bark-dark:#4a260c;
  --panel:#7a4214;
  --panel-edge:#5a2e0e;
  --orange:#f0a52a;
  --gold:#f7c25b;
  --cream:#f4e6cf;
  --text:#efe6da;
  --sign:#c9822f;
  --sign-edge:#8a4f16;
  --sign-text:#f6c9e0;
  --btn:#6f6a63;
  --parchment:#e0a457;
  --link:#7fb3e0;
  --cross:#c0262a;
}
*{box-sizing:border-box;margin:0;padding:0}
html,body{width:1200px;height:2219px;overflow:hidden;background:var(--bg)}
body{position:relative;font-family:'Quicksand',sans-serif;color:var(--text)}
.abs{position:absolute}
.fill{position:absolute;border-radius:4px}

/* header */
.site-title{left:440px;top:16px;width:720px;text-align:center;white-space:nowrap;font-family:'Bangers',sans-serif;font-size:58px;line-height:1.1;letter-spacing:2px;color:var(--orange);text-shadow:0 3px 4px #000}
.nav-btn{position:absolute;height:45px;display:flex;align-items:center;justify-content:center;white-space:nowrap;background:linear-gradient(#b86a22,#8a4812);border:2px solid #3a1e08;box-shadow:inset 0 0 0 2px #c97c30;font-family:'Exo 2',sans-serif;font-style:italic;font-size:16px;color:#fff3d6;text-shadow:0 1px 2px #000}

/* brand */
.brand-art{left:60px;top:15px;width:370px;height:150px;background:radial-gradient(ellipse at 50% 70%,#2f7a2a,#184d1a 60%,transparent 72%)}
.brand-name{left:30px;top:168px;width:440px;text-align:center;white-space:nowrap;font-family:'Quicksand',sans-serif;font-weight:600;font-size:54px;line-height:1;color:#ffffff}
.brand-tag{left:40px;top:280px;width:400px;text-align:center;white-space:nowrap;font-family:'Quicksand',sans-serif;font-weight:600;font-size:18px;color:var(--gold);transform:rotate(-8deg)}

/* hero */
.hero{left:22px;top:222px;width:1155px;height:385px;background:var(--bark);border:3px solid var(--bark-dark)}
.hero-left{left:32px;top:232px;width:410px;height:365px;background:var(--panel);border-radius:6px;box-shadow:inset 0 0 12px #3a1c06}
.hero-copy{left:244px;top:352px;width:190px;font-size:13.5px;line-height:1.3;color:#fff}
.hero-copy .tail{display:block;margin-left:-110px;text-indent:40px;width:300px}
.price-sign{left:12px;top:340px;width:232px;height:130px;background:var(--sign);border:3px solid var(--sign-edge);border-radius:10px 4px 14px 6px;transform:rotate(-3deg);display:flex;align-items:center;justify-content:center;text-align:center;font-family:'Rye',serif;font-size:24px;line-height:1.15;color:var(--sign-text);text-shadow:0 2px 0 #6a2c58}
.btn{position:absolute;display:flex;align-items:center;justify-content:center;white-space:nowrap;background:linear-gradient(#8a857d,#5d5851);border:2px solid #a9a49b;border-radius:8px;font-family:'Rosarivo',serif;font-size:20px;color:#fff;box-shadow:0 2px 4px #000}
.slide{left:447px;top:229px;width:722px;height:366px;background:linear-gradient(160deg,#4f5a3a,#7c8c86 45%,#cfd6d4 55%,#5d5d4c 80%,#3e3a2c)}
.slide-caption{left:459px;top:481px;width:536px;height:89px;background:rgba(70,70,70,.55)}
.slide-caption h3{position:absolute;left:12px;top:6px;font-family:'Sancreek',serif;font-weight:400;font-size:26px;color:#fff;letter-spacing:1px;white-space:nowrap}
.slide-caption p{position:absolute;left:50px;top:42px;width:470px;font-size:16px;line-height:1.3;text-indent:40px;color:#fff}
.arrow{top:360px;width:30px;height:90px}

/* tour inclusions */
.section-title{font-family:'Rye',serif;font-weight:400;font-size:31px;color:var(--gold);text-shadow:0 2px 3px #000;white-space:nowrap}
.thumb{position:absolute;width:93px;height:96px;border:1px solid #000}
.signpost{position:absolute;background:var(--sign);border:3px solid var(--sign-edge);border-radius:8px 3px 10px 4px;display:flex;align-items:center;justify-content:center;text-align:center;font-family:'Rye',serif;color:var(--sign-text);text-shadow:0 2px 0 #6a2c58;line-height:1.2;white-space:nowrap}
.feature{position:absolute;left:18px;width:690px;height:96px}
.feature .pic{position:absolute;left:0;top:0;width:93px;height:93px}
.feature h4,.lead h4{position:absolute;left:108px;top:8px;font-style:italic;font-weight:600;font-size:15px;color:var(--orange);white-space:nowrap}
.feature p,.lead p{position:absolute;left:108px;top:30px;width:560px;font-size:14.5px;line-height:1.3;text-indent:36px;color:#fff}
.lead{position:absolute;left:40px;top:806px;width:660px;height:60px}
.lead h4{left:0;top:0}
.lead p{left:0;top:22px;width:620px}

/* sidebar */
.sidebar{left:731px;top:836px;width:443px;height:1029px;background:var(--panel);border:3px solid var(--panel-edge)}
.side-title{position:absolute;font-family:'Rye',serif;font-weight:400;font-size:23px;color:var(--gold);text-shadow:0 2px 3px #000;white-space:nowrap}
.calendar{left:784px;top:910px;width:356px;height:237px;background:var(--parchment);border:3px solid #8a4f16;border-radius:10px;box-shadow:0 3px 6px #000}
.cal-head{position:absolute;left:0;top:14px;width:100%;text-align:center;font-family:'Rosarivo',serif;font-size:24px;color:#4a260c}
.cal-table{position:absolute;left:22px;top:52px;width:312px;border-collapse:collapse;text-align:center;color:#fff;font-size:19px}
.cal-table th{font-size:13px;font-weight:500;color:#4a260c;height:22px}
.cal-table td{height:27px;position:relative}
.cross{color:var(--cross);font-weight:600}
.gallery-pic{position:absolute;top:1288px;width:122px;height:132px}
.gallery-frame{left:755px;top:1283px;width:396px;height:138px;background:#4a260c}
.testi-box{left:747px;top:1557px;width:412px;height:287px;background:#5a2f10;border-radius:8px}
.testi{position:absolute;left:55px;width:340px;font-size:14.5px;line-height:1.22;color:#fff}
.leaf{position:absolute;left:16px;width:30px;height:30px}

/* footer */
.footer{left:0;top:2079px;width:1200px;height:140px;background:radial-gradient(ellipse at 50% 40%,#3a2616,var(--bg) 60%)}
.footer-nav{position:absolute;left:0;top:36px;width:100%;display:flex;justify-content:center;font-size:17px;color:var(--link)}
.footer-nav span{padding:0 18px;border-left:1px solid #5a4634}
.footer-nav span:first-child{border-left:0}
.copyright{position:absolute;left:0;top:70px;width:100%;text-align:center;font-size:16px;color:#fff;letter-spacing:.5px}
</style>
</head>
<body>

<header>
  <div class="abs site-title">CAPE TRIBULATION AND CAIRNS</div>
  <nav>
    <div class="nav-btn" style="left:496px;top:105px;width:137px">HOME</div>
    <div class="nav-btn" style="left:653px;top:105px;width:139px">ACCOMODATION</div>
    <div class="nav-btn" style="left:811px;top:105px;width:139px">BOOK ONLINE</div>
    <div class="nav-btn" style="left:969px;top:105px;width:139px">CONTACT US</div>
    <div class="nav-btn" style="left:647px;top:165px;width:308px">AUTHENTIC ABORIGINAL ART FOR SALE</div>
  </nav>
</header>

<section class="hero-area">
  <div class="abs hero"></div>
  <div class="abs hero-left"></div>
  <div class="abs slide" role="img" aria-label="Photo of Crystal Cascades waterfall among rainforest rocks"></div>
  <svg class="abs arrow" style="left:458px" viewBox="0 0 30 90"><path d="M22 15 L8 45 L22 75" fill="none" stroke="rgba(255,255,255,.6)" stroke-width="4"/></svg>
  <svg class="abs arrow" style="left:1130px" viewBox="0 0 30 90"><path d="M8 15 L22 45 L8 75" fill="none" stroke="rgba(255,255,255,.6)" stroke-width="4"/></svg>
  <div class="abs slide-caption">
    <h3>CRYSTAL CASCADE</h3>
    <p>Crystals is a secluded freshwater swimming hole, hidden in a tropical world heritage listed rainforest.</p>
  </div>

  <div class="fill brand-art" role="img" aria-label="Illustration of a rainforest bird among palm leaves and butterflies"></div>
  <div class="abs brand-name">Meadow Lantern</div>
  <div class="abs brand-tag">A taste of true authentic Aboriginal Culture</div>

  <div class="abs price-sign">ONLY $249<br>TWO DAYS &amp;<br>ONE NIGHT</div>
  <p class="abs hero-copy">Experience true local Indigenous Culture. By twilight 0traditional Aboriginal food cooking methods and taste testing, demonstration spear and Boomerang throwing!<span class="tail">Didjeereedoo playing lessons by a bon fire, dream time stories under the stars!</span></p>
  <div class="btn" style="left:286px;top:533px;width:145px;height:50px">Read more</div>
</section>

<main>
  <h2 class="abs section-title" style="left:195px;top:626px">TOUR INCLUSIONS</h2>
  <div class="thumb" style="left:104px;top:696px;background:linear-gradient(#3d6a34,#6f8a6a)" role="img" aria-label="Tour boat on the river"></div>
  <div class="thumb" style="left:212px;top:696px;background:linear-gradient(#6a6052,#403a30)" role="img" aria-label="Lizard on a branch"></div>
  <div class="thumb" style="left:320px;top:696px;background:linear-gradient(#1a1a1a,#4a4a3a)" role="img" aria-label="Crocodile with open jaws"></div>
  <div class="thumb" style="left:428px;top:696px;background:linear-gradient(#8c8b70,#3e5a7a)" role="img" aria-label="Kookaburra perched"></div>
  <div class="thumb" style="left:539px;top:696px;background:linear-gradient(#c8621c,#3a6b22)" role="img" aria-label="Frog on tropical flowers"></div>

  <div class="fill" style="left:710px;top:700px;width:474px;height:136px;background:linear-gradient(transparent,#2f5a1c 55%,#1f3a12)" role="img" aria-label="Illustration of grass, hiking boots and a backpack"></div>
  <div class="signpost" style="left:666px;top:648px;width:237px;height:84px;font-size:23px;transform:rotate(-4deg)">TRUE LOCAL<br>GUIDES !</div>
  <div class="signpost" style="left:888px;top:572px;width:289px;height:144px;font-size:21px">TRAVEL IN A<br>SMALL EXCLUSIVE<br>INTERMIT GROUP<br>13 OR LESS</div>

  <article class="lead">
    <h4>Crocodile Sighting</h4>
    <p>Jump on board a boat and explore the notorious Croc infested "Daintree River!" Sight seeing Crocodiles, bird life, and extensive marine life existing in the river!</p>
  </article>

  <article class="feature" style="top:900px"><div class="pic fill" style="background:linear-gradient(#7a8a6a,#c8d0c8 50%,#4a5a3a)" role="img" aria-label="Waterfall photo"></div><h4>Folk 'Cascading Crystal'</h4><p>Visit Crystal Cascades one of the secrets of North Queensland that locals have kept hidden from visitors. Crystals is a secluded freshwater swimming hole, hidden in a tropical world heritage listed rainforest.</p></article>
  <article class="feature" style="top:1009px"><div class="pic fill" style="background:linear-gradient(#5a6a4a,#2f3a28)" role="img" aria-label="People fishing in the bush"></div><h4>Barramudi Catching</h4><p>Experience the thrill and excitement of catching Australia's most iconic prize fighting fish!</p></article>
  <article class="feature" style="top:1117px"><div class="pic fill" style="background:linear-gradient(#2f6a2a,#5a8a3a)" role="img" aria-label="Rainforest lookout walkway"></div><h4>Scenic Lookout</h4><p>Thorton Peak Lookout. Stop and enjoy the view of the oldest low lying Rainforest in the world!</p></article>
  <article class="feature" style="top:1225px"><div class="pic fill" style="background:#6b3813" role="img" aria-label="Knife icon on brown tile"></div><h4>Aboriginal Food Taste Testing</h4><p>Experience Aboriginal food taste testing and authentic cooking methods on the beach.</p></article>
  <article class="feature" style="top:1335px"><div class="pic fill" style="background:linear-gradient(#1a1410,#a04a14 70%,#2a1a10)" role="img" aria-label="Bonfire at night"></div><h4>Didjeereedo Playing</h4><p>Spend 3 hours with a local Aboriginal guide listening to the amazing sound of a didjeereedoo! Experience a twilight beach bonfire hearing dream time stories under the stars!</p></article>
  <article class="feature" style="top:1443px"><div class="pic fill" style="background:radial-gradient(#e0701a,#5a1a08 60%,#140a06)" role="img" aria-label="Campfire flames"></div><h4>Mud Crab Catching</h4><p>Fish off the beach in a small group with local guides!</p></article>
  <article class="feature" style="top:1551px"><div class="pic fill" style="background:linear-gradient(#6a8a6a,#a8a89a 50%,#3a4a3a)" role="img" aria-label="River among rocks in a gorge"></div><h4>Mossman Gorge</h4><p>Take a refreshing swim in the beautiful Mossman Gorge mountain river!</p></article>
  <article class="feature" style="top:1659px"><div class="pic fill" style="background:linear-gradient(#6aa8e0,#2a8ab0 55%,#3a6a3a)" role="img" aria-label="Coastal town view"></div><h4>Port Douglas</h4><p>Visit the famous and funky touristic town of Port Douglas!</p></article>
  <article class="feature" style="top:1767px"><div class="pic fill" style="background:linear-gradient(#8ab8e0,#3a6a3a 60%,#4a8aa0)" role="img" aria-label="Beach with trees"></div><h4>Ellis Beach</h4><p>Visit the beautiful Ellis beach</p></article>
  <article class="feature" style="top:1875px"><div class="pic fill" style="background:linear-gradient(#8ac0e8,#2a90b8 60%,#1a6a8a)" role="img" aria-label="Ocean and sky"></div><h4>Palm Cove</h4><p>Take a brief walk along the spectacular beach of Palm cove! Enjoy the serenity and take beautiful photos!</p></article>
  <article class="feature" style="top:1983px"><div class="pic fill" style="background:linear-gradient(#a8c0d0,#6a8a4a 55%,#5a7a3a)" role="img" aria-label="Grassy field with wallabies"></div><h4>Wallaby Kangaroo Sightseeing</h4><p>A brief stop to experience a large local Wallaby group at Trinity beach</p></article>
</main>

<aside>
  <div class="abs sidebar"></div>
  <h3 class="side-title" style="left:820px;top:856px">AVAILABILITY CALENDAR</h3>
  <div class="abs calendar">
    <div class="cal-head">&#9664;&nbsp;&nbsp; June 2015 &nbsp;&nbsp;&#9654;</div>
    <table class="cal-table">
      <tr><th>Sun</th><th>Mon</th><th>Tues</th><th>Wed</th><th>Thurs</th><th>Fri</th><th>Sat</th></tr>
      <tr><td></td><td>1</td><td>2</td><td>3</td><td>4</td><td class="cross">&#10006;</td><td>6</td></tr>
      <tr><td>7</td><td>8</td><td>9</td><td>10</td><td>11</td><td>12</td><td>13</td></tr>
      <tr><td>14</td><td class="cross">&#10006;</td><td>16</td><td>17</td><td>18</td><td>19</td><td>20</td></tr>
      <tr><td>21</td><td>22</td><td>23</td><td class="cross">&#10006;</td><td>25</td><td>26</td><td>27</td></tr>
      <tr><td>28</td><td>29</td><td>30</td><td></td><td></td><td></td><td></td></tr>
    </table>
  </div>
  <div class="btn" style="left:1027px;top:1165px;width:121px;height:47px">Book Now!</div>

  <h3 class="side-title" style="left:754px;top:1234px">CHECK OUT OUR GALLERY</h3>
  <div class="abs gallery-frame"></div>
  <div class="gallery-pic" style="left:759px;background:linear-gradient(#2f6a2a,#6a8a4a)" role="img" aria-label="Rainforest walkway"></div>
  <div class="gallery-pic" style="left:889px;background:linear-gradient(#2a2a2a,#3a6ab0 60%,#1a1a1a)" role="img" aria-label="Kingfisher bird"></div>
  <div class="gallery-pic" style="left:1019px;background:linear-gradient(#3a1a0a,#b0601a 60%,#2a140a)" role="img" aria-label="Candle-lit interior"></div>
  <div class="btn" style="left:1027px;top:1446px;width:121px;height:47px">Click here!</div>

  <h3 class="side-title" style="left:754px;top:1514px">TESTIMONIALS</h3>
  <div class="abs testi-box">
    <svg class="leaf" style="top:16px" viewBox="0 0 30 30"><path d="M15 2 L18 11 L28 9 L21 16 L27 25 L15 20 L3 25 L9 16 L2 9 L12 11 Z" fill="#3f8a2a"/></svg>
    <p class="testi" style="top:13px">Lorem ipsum dolor sit amet, consectetuer adipiscing elit. Aenean commodo ligula eget dolor. Aenean massa.</p>
    <svg class="leaf" style="top:84px" viewBox="0 0 30 30"><path d="M15 2 L18 11 L28 9 L21 16 L27 25 L15 20 L3 25 L9 16 L2 9 L12 11 Z" fill="#3f8a2a"/></svg>
    <p class="testi" style="top:82px">Lorem ipsum dolor sit amet, consectetuer adipiscing elit. Aenean commodo ligula eget dolor. Aenean massa.</p>
    <svg class="leaf" style="top:152px" viewBox="0 0 30 30"><path d="M15 2 L18 11 L28 9 L21 16 L27 25 L15 20 L3 25 L9 16 L2 9 L12 11 Z" fill="#3f8a2a"/></svg>
    <p class="testi" style="top:149px">Lorem ipsum dolor sit amet, consectetuer adipiscing elit. Aenean commodo ligula eget dolor. Aenean massa.</p>
    <svg class="leaf" style="top:220px" viewBox="0 0 30 30"><path d="M15 2 L18 11 L28 9 L21 16 L27 25 L15 20 L3 25 L9 16 L2 9 L12 11 Z" fill="#3f8a2a"/></svg>
    <p class="testi" style="top:218px">Lorem ipsum dolor sit amet, consectetuer adipiscing elit. Aenean commodo ligula eget dolor. Aenean massa.</p>
  </div>
</aside>

<footer class="abs footer">
  <div class="footer-nav"><span>Home</span><span>Accomodation</span><span>Book Online</span><span>Contact Us</span></div>
  <p class="copyright">Copyright © 2015. Meadow Lantern. All Rights Reserve</p>
</footer>

</body>
</html>
```